Professional website for psychological services

Create a professional, easy to navigate website using soothing coastal images and incorporate company logo in design. Website is for a small private clinic that provides psychological services and must be appealing to professional men and women. A website I really like is www.velmorlodge.example I would love something like similar.

Target Market(s)

Professional men and women seeking psychological services

Industry/Entity Type

Mental Health

Number of Pages Required

5+ page

Requirements
Must have
• The website must incorporate the logo provided. The name of the company/website is Brindle Oak Wellness Aftercare. Colors must compliment the logo, must be coastal and soothing yet very professional. I would like a website like www.velmorlodge.example
• Pages will be:Home, Services, FAQ and Contact Us. The images included of the building and office are for the contact us page. Under the tab Servies: Individual Psychotherapy, Family Therapy, EMDR I will provide specific content for each.
Nice to have
• I want the website to be easy to navigate and the font easy to read. The writing on the logo is very light and I'm open to changing it slightly if it will be better aesthetically.
Should not have
• Please no pictures of any swimsuits, alcoholic beverages, etc. This is a professional psychological clinic.

```html
<!DOCTYPE html>
<html lang="en">
<head>
<meta charset="utf-8">
<title>Brindle Oak Wellness Aftercare</title>
<link href="https://fonts.googleapis.com/css2?family=Mulish:wght@400;600&family=Great+Vibes&display=swap" rel="stylesheet">
<style>
:root{
  --aqua:#29b6d5;
  --aqua-dark:#1a9fbf;
  --ink:#1c1c1c;
  --muted:#6b6b6b;
  --white:#ffffff;
  --field:#f1f1f1;
  --field-edge:#d9d9d9;
  --sand:#e3d5c0;
  --night:#050505;
  --stage:#eef1f2;
  --sea-deep:#27525a;
  --sea-mid:#3f7377;
  --dusk:#6b4d45;
  --peach:#e9a380;
}
*{box-sizing:border-box;margin:0;padding:0}
html,body{width:1200px;height:1200px;overflow:hidden;background:var(--stage)}
body{font-family:"Mulish",sans-serif;color:var(--ink)}
.page{position:absolute;left:364px;top:0;width:541px;height:1370px;transform:scale(0.8755);transform-origin:0 0;background:var(--white);box-shadow:0 0 18px rgba(0,0,0,.12);overflow:hidden}
.abs{position:absolute}

/* header */
.site-header{left:0;top:0;width:541px;height:111px;background:var(--white)}
.brand{left:0;top:28px;width:541px;text-align:center}
.brand-name{font-size:22px;color:var(--aqua);font-weight:400;letter-spacing:.5px}
.brand-tag{font-size:5px;color:#b9b9b9;letter-spacing:1.5px;text-transform:uppercase;margin-top:3px}
.brand-dot{display:inline-block;width:9px;height:9px;border-radius:50%;background:var(--aqua);margin-right:6px;vertical-align:middle}
.main-nav{top:89px;left:0;width:541px;display:flex;justify-content:center;gap:18px;font-size:7px}
.main-nav .current{color:var(--aqua)}

/* hero */
.hero{left:0;top:111px;width:541px;height:226px;background:linear-gradient(180deg,#4b6d6e 0%,var(--sea-deep) 35%,var(--sea-mid) 60%,var(--dusk) 100%)}
.portrait{border-radius:50%;border:4px solid var(--aqua);background:radial-gradient(circle at 50% 40%,#b69480 0%,#5a4034 55%,#3d5a35 100%)}
.hero .portrait{left:30px;top:30px;width:134px;height:134px}
.quote{left:186px;top:65px;width:185px;font-size:10.5px;line-height:12.5px;color:var(--white)}
.quote-author{left:240px;top:104px;font-family:"Great Vibes",cursive;font-size:17px;color:var(--white)}
.arrow-nav{color:var(--aqua);font-size:14px;font-weight:600}
.slide{background:linear-gradient(135deg,#8c6a52,#c9b79b 55%,#5d4536)}
.slide-alt{background:linear-gradient(180deg,#9fb9c4,#5d7a58 60%,#b0a592)}
.thumb{width:31px;height:31px}
.thumb.active{outline:2px solid var(--aqua)}

/* about */
.section-title{left:0;width:541px;text-align:center;text-transform:uppercase}
.about-title{top:382px;font-size:19px}
.about-copy{left:60px;top:422px;width:421px;text-align:center;font-size:8.6px;line-height:19px}
.btn{height:24px;border-radius:4px;font-size:8px;text-transform:uppercase;display:flex;align-items:center;justify-content:center}
.btn-fill{background:var(--aqua);color:var(--white);box-shadow:0 1px 3px rgba(0,0,0,.25)}
.btn-line{border:2px solid var(--aqua);color:var(--aqua);background:var(--white)}

/* services */
.services{left:0;top:555px;width:541px;height:304px;background:linear-gradient(180deg,#5f7d7c 0%,#35605f 30%,#3f5e5a 55%,#6a4b3f 78%,var(--dusk) 100%)}
.beach{left:0;top:226px;width:541px;height:78px;background:linear-gradient(100deg,#5fb0b3 0%,#8cc6c1 35%,#e7b196 58%,var(--peach) 100%)}
.services-title{top:56px;font-size:17px;color:#f1ece6}
.service{top:93px;width:140px;color:var(--white)}
.service h3{font-size:13px;font-weight:400;text-transform:uppercase;margin-bottom:4px}
.service p{font-size:8.3px;line-height:19px}
.service .more{color:#d8d0c8}

/* contact */
.contact-title{top:907px;font-size:17px}
.contact .portrait{left:69px;top:961px;width:134px;height:134px}
.field{left:220px;width:258px;height:24px;background:var(--field);border-bottom:2px solid var(--field-edge);border-right:2px solid var(--field-edge);color:var(--aqua);font-size:12.5px;padding:3px 0 0 18px}
.address{left:71px;top:1162px;font-size:12.5px;line-height:23px}
.enquiries{left:335px;top:1162px;font-size:12.5px;line-height:23px}
.enquiries .label{color:var(--muted)}

/* newsletter + footer */
.newsletter{left:0;top:1274px;width:541px;height:56px;background:var(--sand)}
.news-label{left:79px;top:23px;font-size:8px}
.news-input{left:207px;top:16px;width:184px;height:24px;background:var(--white);font-size:7.5px;color:var(--aqua);padding:8px 0 0 18px}
.news-send{left:391px;top:16px;width:73px;height:24px;background:var(--aqua);color:var(--white);font-size:8px;display:flex;align-items:center;justify-content:center}
.site-footer{left:0;top:1330px;width:541px;height:40px;background:var(--night);color:var(--white);font-size:7px}
.social{width:14px;height:14px;border-radius:50%;background:var(--aqua-dark)}
</style>
</head>
<body>
<main class="page">

  <header class="site-header abs">
    <div class="brand abs">
      <div class="brand-name"><span class="brand-dot"></span>Brindle Oak</div>
      <div class="brand-tag">Brindle Oak Wellness Aftercare</div>
    </div>
    <nav class="main-nav abs">
      <span class="current">Home</span><span>Services</span><span>FAQ</span><span>Contact Us</span>
    </nav>
  </header>

  <section class="hero abs">
    <div class="portrait abs" role="img" aria-label="Portrait photograph of the clinic's psychologist"></div>
    <p class="quote abs">"Lorem ipsum dolor sit amet, consectetur adipiscing elit, sed do eiusmod tempor incididunt ut"</p>
    <p class="quote-author abs">Author's Name</p>
    <span class="arrow-nav abs" style="left:360px;top:30px">&lsaquo;</span>
    <span class="arrow-nav abs" style="left:387px;top:30px">&rsaquo;</span>
    <div class="slide abs" role="img" aria-label="Photograph of the clinic office interior" style="left:364px;top:51px;width:111px;height:110px"></div>
    <div class="slide-alt abs" role="img" aria-label="Photograph of the clinic building with palm trees" style="left:479px;top:51px;width:62px;height:110px"></div>
    <div class="thumb active slide abs" role="img" aria-label="Thumbnail of office interior" style="left:364px;top:168px"></div>
    <div class="thumb slide-alt abs" role="img" aria-label="Thumbnail of clinic building" style="left:401px;top:168px"></div>
    <div class="thumb abs" role="img" aria-label="Thumbnail of coastal bay" style="left:439px;top:168px;background:linear-gradient(180deg,#3d7fc0,#1f6d9a 55%,#d9e4e6)"></div>
    <div class="thumb abs" role="img" aria-label="Thumbnail of seaside view" style="left:475px;top:168px;background:linear-gradient(180deg,#d9d2c2,#9fa79b)"></div>
    <div class="thumb abs" role="img" aria-label="Thumbnail of sunset silhouette" style="left:513px;top:168px;background:linear-gradient(90deg,#f2efe9,#e2a25a 60%,#3a2a22)"></div>
    <svg class="abs" style="left:264px;top:182px" width="16" height="20" viewBox="0 0 16 20" aria-hidden="true">
      <path d="M8 1v17M2 12l6 6 6-6" fill="none" stroke="#fff" stroke-width="1.6"/>
    </svg>
  </section>

  <section class="about">
    <h2 class="section-title about-title abs" style="font-weight:400">About Brindle Oak</h2>
    <p class="about-copy abs">Lorem ipsum dolor sit amet, consectetur adipiscing elit, sed do eiusmod tempor incididunt ut labore et dolore magna aliqua. Ut enim ad minim veniam, quis nostrud exercitation ullamco laboris nisi ut aliquip ex ea commodo consequat. Duis aute irure.</p>
    <span class="btn btn-fill abs" style="left:183px;top:489px;width:77px">Contact Us</span>
    <span class="btn btn-line abs" style="left:283px;top:489px;width:77px">Learn More</span>
  </section>

  <section class="services abs" role="img" aria-label="Coastal photograph of a calm bay with an island and sandy shore">
    <div class="beach abs"></div>
    <h2 class="section-title services-title abs" style="font-weight:400">Services</h2>
    <div class="service abs" style="left:58px">
      <h3>Speaking</h3>
      <p>Lorem ipsum dolor sit amet, consectetur adipiscing elit, sed do eiusmod tempor incididunt ut <span class="more">learn more...</span></p>
    </div>
    <div class="service abs" style="left:211px">
      <h3>Training</h3>
      <p>Lorem ipsum dolor sit amet, consectetur adipiscing elit, sed do eiusmod tempor incididunt ut <span class="more">learn more...</span></p>
    </div>
    <div class="service abs" style="left:364px">
      <h3>Check Up</h3>
      <p>Lorem ipsum dolor sit amet, consectetur adipiscing elit, sed do eiusmod tempor incididunt ut <span class="more">learn more...</span></p>
    </div>
  </section>

  <section class="contact">
    <h2 class="section-title contact-title abs" style="font-weight:400">Get in Touch</h2>
    <div class="portrait abs" role="img" aria-label="Portrait photograph of the clinic's psychologist"></div>
    <div class="field abs" style="top:958px">NAME *</div>
    <div class="field abs" style="top:986px">EMAIL *</div>
    <div class="field abs" style="top:1014px">PHONE NUMBER *</div>
    <div class="field abs" style="top:1042px;height:54px">MESSAGE *</div>
    <span class="btn btn-fill abs" style="left:400px;top:1106px;width:77px">Send</span>
    <address class="address abs" style="font-style:normal">#4/1 Harbour Lane,<br>PH 55080,<br>Quay Bus Stop</address>
    <div class="enquiries abs">
      <div class="label">PHONE</div>
      <div>08105550142</div>
      <div class="label">GENERAL ENQUIRIES</div>
      <div>hello@brindleoak.example</div>
    </div>
  </section>

  <section class="newsletter abs">
    <span class="news-label abs">Subscribe to our newsletter</span>
    <span class="news-input abs">hello@brindleoak.example</span>
    <span class="news-send abs">SEND</span>
  </section>

  <footer class="site-footer abs">
    <span class="abs" style="left:71px;top:15px">© 2018 Brindle Oak</span>
    <span class="abs" style="left:384px;top:15px">Terms</span>
    <span class="abs" style="left:413px;top:15px">Privacy</span>
    <span class="social abs" style="left:446px;top:13px"></span>
    <span class="social abs" style="left:469px;top:13px"></span>
    <span class="social abs" style="left:492px;top:13px"></span>
  </footer>

</main>
</body>
</html>
```